Emergency Medical Training and Events Company Business Needs Business Card Design

We are in need of a business card for our dynamic company expanding its customer base and need to be easily contacted and identified for when we visit with government officials, potential EMS / Fire agencies and county coordinators to arrange for training programs for first responders to better prepare them for critical thinking at critical incidents.

Target Market(s)

EMS/Fire and Event Promoters

Industry/Entity Type

Medical

Contact Information for Business Card

Two cards, comparable designs:

Martin K. Halvey, Principal, m.halvey@rvqtlo.com
Owen Tash, Event and Training Specialist, o.tash@rvqtlo.com

Font styles to use
Other font styles liked:
• Cambria

Colors

Designer to choose colors to be used in the design.

Requirements
Must have
• Company Logo, Spots for Name, Title, Phone Number, Email, Website
• A bullet list stating that we offer, QRB CPR and First Aid Instructors, Hold the Line Instructors, Event EMS, CME's, MCI Training and Planning. We prefer to have a black background for the card but if you can make a blue or white card stand out we would review that as well.
Should not have
• Tacky logos or special sayings ... simple, elegant, professional is the look we seek

```html
<!DOCTYPE html>
<html lang="en">
<head>
<meta charset="utf-8">
<title>RVQTLO Business Card</title>
<link href="https://fonts.googleapis.com/css2?family=Montserrat:wght@400;500;800&display=swap" rel="stylesheet">
<style>
  :root {
    --navy: #0c1f6b;
    --navy-deep: #081552;
    --red: #c8202a;
    --ink: #3a3a3a;
    --paper: #ffffff;
    --backdrop: #e4e5e8;
  }
  * { box-sizing: border-box; margin: 0; padding: 0; }
  html, body { width: 1200px; height: 900px; overflow: hidden; }
  body {
    background: var(--backdrop);
    font-family: "Montserrat", Arial, sans-serif;
    display: flex;
    flex-direction: column;
    align-items: center;
    justify-content: center;
    gap: 40px;
  }
  .card {
    width: 700px;
    height: 400px;
    position: relative;
    box-shadow: 0 8px 24px rgba(0,0,0,.18);
  }
  .card-front {
    background: linear-gradient(135deg, #f4f4f4 0%, var(--paper) 60%);
  }
  .brand-mark {
    position: absolute;
    left: 60px;
    top: 172px;
    width: 260px;
    display: flex;
    align-items: center;
    gap: 16px;
  }
  .brand-dot {
    width: 56px; height: 56px;
    border-radius: 50%;
    background: var(--red);
    flex: none;
  }
  .brand-name {
    font-weight: 800;
    font-size: 40px;
    letter-spacing: 2px;
    color: var(--navy);
  }
  .divider {
    position: absolute;
    left: 350px;
    top: 85px;
    width: 3px;
    height: 230px;
    background: var(--red);
  }
  .contact {
    position: absolute;
    left: 380px;
    top: 80px;
    right: 30px;
    color: var(--ink);
  }
  .person-name {
    font-weight: 800;
    font-size: 30px;
    color: var(--red);
    text-transform: uppercase;
    letter-spacing: 1px;
    line-height: 1;
  }
  .person-title {
    font-size: 16px;
    font-weight: 500;
    margin: 6px 0 14px;
  }
  .contact-list { list-style: none; }
  .contact-list li {
    display: flex;
    align-items: center;
    gap: 9px;
    font-size: 16px;
    line-height: 26px;
  }
  .contact-list svg { width: 14px; height: 14px; flex: none; }
  .company-legal {
    font-size: 15px;
    line-height: 20px;
    margin-top: 8px;
  }
  .card-back {
    background: linear-gradient(135deg, var(--navy) 0%, var(--navy-deep) 100%);
    color: #ffffff;
  }
  .back-mark {
    position: absolute;
    left: 0; right: 0;
    top: 50px;
    display: flex;
    align-items: center;
    justify-content: center;
    gap: 24px;
  }
  .back-dot {
    width: 84px; height: 84px;
    border-radius: 50%;
    background: #ffffff;
  }
  .back-rule {
    width: 3px; height: 110px;
    background: var(--red);
  }
  .back-name {
    font-weight: 800;
    font-size: 60px;
    letter-spacing: 4px;
    color: #ffffff;
  }
  .services {
    position: absolute;
    left: 70px; right: 70px;
    top: 222px;
    list-style: none;
    display: grid;
    grid-template-columns: 1fr 1fr;
    column-gap: 30px;
    row-gap: 12px;
  }
  .services li {
    display: flex;
    align-items: center;
    gap: 10px;
    font-size: 16px;
    font-weight: 500;
    line-height: 22px;
  }
  .services li::before {
    content: "";
    width: 8px; height: 8px;
    border-radius: 50%;
    background: var(--red);
    flex: none;
  }
</style>
</head>
<body>
  <section class="card card-front">
    <div class="brand-mark">
      <span class="brand-dot"></span>
      <span class="brand-name">RVQTLO</span>
    </div>
    <div class="divider"></div>
    <div class="contact">
      <h1 class="person-name">Owen Tash</h1>
      <p class="person-title">Event and Training Specialist</p>
      <ul class="contact-list">
        <li>
          <svg viewBox="0 0 16 16"><path d="M4 1l3 3-2 2c1 2 3 4 5 5l2-2 3 3-2 3C7 15 1 9 1 3z" fill="var(--red)"/></svg>
          555.014.2002
        </li>
        <li>
          <svg viewBox="0 0 16 16"><rect x="4" y="1" width="8" height="14" rx="1.5" fill="none" stroke="var(--red)" stroke-width="1.8"/><circle cx="8" cy="12.5" r="1" fill="var(--red)"/></svg>
          555.019.7890
        </li>
        <li>
          <svg viewBox="0 0 16 16"><rect x="1" y="3" width="14" height="10" fill="none" stroke="var(--red)" stroke-width="1.8"/><path d="M1 3l7 6 7-6" fill="none" stroke="var(--red)" stroke-width="1.8"/></svg>
          o.tash@rvqtlo.com
        </li>
        <li>
          <svg viewBox="0 0 16 16"><circle cx="8" cy="8" r="7" fill="var(--red)"/><path d="M1 8h14M8 1c-3 4-3 10 0 14M8 1c3 4 3 10 0 14" fill="none" stroke="#fff" stroke-width="1"/></svg>
          rvqtlo.com
        </li>
      </ul>
      <p class="company-legal">Rivertide Quality Training<br>&amp; Logistics Solutions<br>of New York, LLC</p>
    </div>
  </section>

  <section class="card card-back">
    <div class="back-mark">
      <span class="back-dot"></span>
      <span class="back-rule"></span>
      <span class="back-name">RVQTLO</span>
    </div>
    <ul class="services">
      <li>QRB CPR and First Aid Instructors</li>
      <li>Hold the Line Instructors</li>
      <li>Event EMS</li>
      <li>CME's</li>
      <li>MCI Training and Planning</li>
    </ul>
  </section>
</body>
</html>
```